Business Card Design Project

I need a business card design for my law office. I already have a logo.

I am an employment attorney who represents clients who have been wrongfully terminated or have been discriminated against by their employer.

I would like a unique, clean design using the colors in the logo or colors that complement the logo.

Target Market(s)

Clients, potential clients, other attorneys and others.

Industry/Entity Type

Attorney

Requirements
Must have
• I would like to use both sides of the card.

The information on the card must be easy to read.

Here is my information:

T. Dale Everhoff
3857 E. Pallister Rd., Suite 204
Fresno, California 93703
559-731-4086
559-862-5143 fax
dale@lawtde.example
Nice to have
• QR Code? I would like to see designs incorporating a nice-looking QR code. Look at this example:

Notice the second QR code in the article - the color.

```html
<!DOCTYPE html>
<html lang="en">
<head>
<meta charset="utf-8">
<title>T. Dale Everhoff Law Office – Business Cards</title>
<link rel="stylesheet" href="https://fonts.googleapis.com/css2?family=Tinos&family=Noto+Sans:wght@400;700&display=swap">
<style>
  :root {
    --backdrop: #262626;
    --card-light: #ffffff;
    --card-edge: #e4e4e4;
    --brand-blue: #2aa8ea;
    --divider: #9a9a9a;
    --ink: #1c1c1c;
  }
  html, body {
    margin: 0;
    padding: 0;
    width: 1200px;
    height: 846px;
    overflow: hidden;
    background: var(--backdrop);
  }
  .stage {
    position: relative;
    width: 1200px;
    height: 846px;
  }
  .card {
    position: absolute;
    width: 592px;
    height: 347px;
    background: radial-gradient(ellipse at 50% 45%, var(--card-light) 30%, var(--card-edge) 100%);
    box-shadow: 0 6px 18px rgba(0,0,0,0.45);
  }
  .card--front { left: 238px; top: 75px; }
  .card--back  { left: 359px; top: 391px; }

  .brand {
    position: absolute;
    display: flex;
    align-items: center;
    color: var(--brand-blue);
    font-family: "Tinos", "Times New Roman", serif;
    font-weight: 400;
  }
  .brand__square {
    background: var(--brand-blue);
    flex: none;
  }
  .brand__rule {
    background: var(--divider);
    flex: none;
  }
  .brand__name {
    line-height: 1;
    white-space: nowrap;
  }
  .brand__sub {
    display: block;
    letter-spacing: 0.22em;
    text-transform: uppercase;
    margin-top: 4px;
    text-align: right;
  }

  .card--front .brand { left: 104px; top: 138px; }
  .card--front .brand__square { width: 56px; height: 56px; }
  .card--front .brand__rule { width: 1px; height: 80px; margin: 0 14px 0 16px; }
  .card--front .brand__name { font-size: 37px; letter-spacing: -0.5px; }
  .card--front .brand__sub { font-size: 14px; }

  .card--back .brand { left: 38px; top: 150px; }
  .card--back .brand__square { width: 32px; height: 32px; }
  .card--back .brand__rule { width: 1px; height: 46px; margin: 0 8px 0 9px; }
  .card--back .brand__name { font-size: 21px; letter-spacing: -0.3px; }
  .card--back .brand__sub { font-size: 8.5px; margin-top: 2px; }

  .contact {
    position: absolute;
    left: 300px;
    top: 112px;
    padding-left: 15px;
    border-left: 2px solid var(--divider);
    height: 129px;
    font-family: "Noto Sans", Verdana, sans-serif;
    font-size: 14.5px;
    line-height: 20.5px;
    color: var(--ink);
  }
  .contact__name {
    font-weight: 700;
    margin: 0 0 3px;
    font-size: 14.5px;
  }
  .contact p { margin: 0; }
</style>
</head>
<body>
<main class="stage">
  <section class="card card--front" aria-label="Card front">
    <div class="brand">
      <span class="brand__square"></span>
      <span class="brand__rule"></span>
      <span class="brand__name">T. Dale Everhoff<span class="brand__sub">Law Office</span></span>
    </div>
  </section>

  <section class="card card--back" aria-label="Card back">
    <div class="brand">
      <span class="brand__square"></span>
      <span class="brand__rule"></span>
      <span class="brand__name">T. Dale Everhoff<span class="brand__sub">Law Office</span></span>
    </div>
    <address class="contact">
      <p class="contact__name">T. Dale Everhoff</p>
      <p>3857 E. Pallister Rd., Suite 204</p>
      <p>Fresno, California 93703</p>
      <p>Tel: 559-731-4086</p>
      <p>Fax: 559-862-5143</p>
      <p>dale@lawtde.example</p>
    </address>
  </section>
</main>
</body>
</html>
```